Business Card Design Project

Same as the logo requirements.
Address of the store is:
Milo's Waypost, LLC
287B North Ferncliff Ave Suite 4
Warren, OH 44592
Gerald Pinkney, Owner

Reason: The design of the business cards should be the same as the main logo.

Reason: I approved the wrong design!

This is the link to the current logo design: http://files.pixelbazaar-example.net/img/720415/391826/391826_5092741_720415_image.jpg

Target Market(s)

Courthouse and downtown employees, including lawyers, judges, downtown office workers.

Industry/Entity Type

Store

Font styles to use
Serif

Requirements
Must have
• Milo's Waypost
A Convenience Store, and More, on Lindenfield Plaza!
Warren, OH 44592
Nice to have
• Colorful, Arrow sign

```html
<!DOCTYPE html>
<html lang="en">
<head>
<meta charset="utf-8">
<title>Milo's Waypost – Business Card</title>
<link rel="stylesheet" href="https://fonts.googleapis.com/css2?family=Courgette&display=swap">
<style>
  :root {
    --wall-dark: #170806;
    --wall-mid: #5e2317;
    --wall-glow: #b2523a;
    --sign-light: #f7dc6e;
    --sign-deep: #e0a92e;
    --sign-red: #a3141b;
    --text-yellow: #f5d24a;
  }
  html, body {
    margin: 0;
    padding: 0;
    width: 686px;
    height: 1200px;
    overflow: hidden;
    background: var(--wall-dark);
  }
  .card {
    position: relative;
    width: 686px;
    height: 1200px;
    overflow: hidden;
    font-family: "Courgette", cursive;
  }
  .brick-wall {
    position: absolute;
    inset: 0;
    background:
      radial-gradient(ellipse 62% 36% at 62% 42%, var(--wall-glow) 0%, var(--wall-mid) 50%, transparent 85%),
      radial-gradient(ellipse 95% 75% at 50% 50%, #4a1a10 0%, #2c0e09 60%, var(--wall-dark) 100%);
  }
  .sign-area {
    position: absolute;
    left: 36px;
    top: 130px;
    width: 604px;
    height: 460px;
    border-radius: 18px;
    background: radial-gradient(ellipse 70% 65% at 60% 45%, var(--sign-light) 0%, var(--sign-deep) 75%, #b9781f 100%);
  }
  .store-name {
    position: absolute;
    left: 190px;
    width: 440px;
    top: 228px;
    margin: 0;
    text-align: center;
    font-size: 100px;
    font-weight: 400;
    line-height: 114px;
    color: var(--sign-red);
  }
  .tagline {
    position: absolute;
    left: 0;
    right: 0;
    top: 632px;
    margin: 0;
    text-align: center;
    font-size: 50px;
    line-height: 66px;
    color: var(--text-yellow);
  }
  .address {
    position: absolute;
    left: 0;
    right: 0;
    top: 1034px;
    margin: 0;
    text-align: center;
    font-style: normal;
    font-size: 38px;
    line-height: 53px;
    color: var(--text-yellow);
  }
</style>
</head>
<body>
  <main class="card">
    <div class="brick-wall" role="img" aria-label="Red brick wall lit by a warm spotlight"></div>

    <div class="sign-area" role="img" aria-label="Illuminated marquee arrow sign carrying the store name"></div>
    <h1 class="store-name">Milo's<br>Waypost</h1>

    <p class="tagline">A Convenience Store,<br>and More,<br>on Lindenfield Plaza!</p>

    <address class="address">287B North Ferncliff Ave Suite 4<br>Warren, OH 44592</address>
  </main>
</body>
</html>
```